Real Estate Managemene Company Needs Business Card Design

We have a logo design and just need business cards made now for our business. Please use PDF logo # 3.

Card with Information to be attached shortly.

The card is used for a real estate management company. We will need to add four other employees and their cards.

Industry/Entity Type

Real Estate

Contact Information for Business Card

Tariq Nawabi
President
3187 Thornfield Avenue
Suite A
Glendale Heights, IL 60847
Phone 630.471.2286
Fax 630.493.7720
Cell 630.517.8043
pvgrop@mailnest.net

Once design is approved we will have four other employees
Omar Nawabi
Operations Manager

Samira Nawabi
Administrative Manager

Faz Nawabi
Principal

We would need to take out the cell # 630.517.8043 out for the remaining three cards.

Requirements
Must have
• Please use logo attached

```html
<!DOCTYPE html>
<html lang="en">
<head>
<meta charset="utf-8">
<title>Meridian Property Management Group – Business Cards</title>
<link href="https://fonts.googleapis.com/css2?family=Open+Sans:wght@400;600;700&display=swap" rel="stylesheet">
<style>
  :root{
    --brand-blue:#0f4f86;
    --card-white:#ffffff;
    --canvas-bg:#e9e6e3;
    --text-light:#ffffff;
  }
  *{box-sizing:border-box;margin:0;padding:0}
  html,body{width:1200px;height:900px;overflow:hidden}
  body{background:var(--canvas-bg);position:relative;font-family:"Open Sans",Arial,sans-serif}

  .card{position:absolute;background:var(--card-white);box-shadow:0 2px 10px rgba(0,0,0,.18);overflow:hidden}

  /* Front */
  .card--front{left:78px;top:34px;width:588px;height:364px}
  .brand{position:absolute;left:32px;top:58px;display:flex;align-items:center;gap:14px;color:var(--brand-blue);font-weight:600}
  .brand__mark{width:52px;height:52px;background:var(--brand-blue);flex:none}
  .brand__name{font-size:19px;line-height:1.25}
  .front__band{position:absolute;left:0;top:156px;width:100%;height:208px;background:var(--brand-blue);color:var(--text-light);padding:6px 0 0 31px}
  .person__name{font-size:19px;font-weight:700;line-height:1.25}
  .person__title{font-size:15px;line-height:1.2;margin-bottom:8px}
  .contact{list-style:none;font-size:15px;line-height:24.5px}
  .contact li{display:flex;align-items:center;gap:6px}
  .contact svg{width:12px;height:12px;fill:var(--text-light);flex:none}
  .contact__address{margin-top:2px}

  /* Back */
  .card--back{left:388px;top:505px;width:567px;height:352px}
  .back__band{position:absolute;left:0;top:110px;width:100%;height:131px;background:var(--brand-blue);display:flex;align-items:center;justify-content:center;color:var(--text-light);font-weight:600}
  .back__name{font-size:26px;line-height:1.3;text-align:center}
</style>
</head>
<body>

<section class="card card--front">
  <div class="brand">
    <span class="brand__mark"></span>
    <div class="brand__name">Meridian<br>Property Management Group</div>
  </div>
  <div class="front__band">
    <p class="person__name">Tariq Nawabi</p>
    <p class="person__title">President</p>
    <ul class="contact">
      <li><svg viewBox="0 0 24 24"><path d="M6.6 10.8a15 15 0 0 0 6.6 6.6l2.2-2.2c.3-.3.7-.4 1-.2 1.1.4 2.3.6 3.6.6.6 0 1 .4 1 1V20c0 .6-.4 1-1 1A17 17 0 0 1 3 4c0-.6.4-1 1-1h3.5c.6 0 1 .4 1 1 0 1.3.2 2.5.6 3.6.1.3 0 .7-.2 1z"/></svg>630.471.2286</li>
      <li><svg viewBox="0 0 24 24"><path d="M6 2h10v6H6zM3 9h18v11H3zm3 3v2h3v-2zm5 0v2h3v-2zm-5 4v2h3v-2zm5 0v2h3v-2z"/></svg>630.493.7720</li>
      <li><svg viewBox="0 0 24 24"><path d="M7 1h10a1 1 0 0 1 1 1v20a1 1 0 0 1-1 1H7a1 1 0 0 1-1-1V2a1 1 0 0 1 1-1zm1 3v15h8V4z"/></svg>630.517.8043</li>
      <li><svg viewBox="0 0 24 24"><path d="M2 5h20v14H2zm2 2v.4l8 5.3 8-5.3V7z"/></svg>pvgrop@mailnest.net</li>
      <li class="contact__address">3187 Thornfield Avenue Suite A Glendale Heights, IL 60847</li>
    </ul>
  </div>
</section>

<section class="card card--back">
  <div class="back__band">
    <div class="back__name">Meridian<br>Property Management Group</div>
  </div>
</section>

</body>
</html>
```